Skip Along Today campaign: promoting kids play in the UK - Website Redesign

Skip Along Today is a national UK campaign that promotes the value of play for children. The current website is live at http://www.skipalongtoday.co.uk. This website has been live for 4 years and now needs to be redesigned. The target audience is parents of young children up to the age of 12.

The current site was designed with a series of old adverts in mind. Here is an example of an old advert: http://vidbox.example/qR7tLm2WxZa

Criticisms of existing site:
The design represented the adverts too closely. The result was a website that mirrors the adverts rather than complements them.
The color scheme is too dark.
Text-heavy pages (e.g. http://www.skipalongtoday.co.uk/fun.php) are dull and not FUN!

New site
We have recently had a series of new video adverts produced:
advert 1: http://vidbox.example/h3JkV9sNbQe
advert 2: http://vidbox.example/Wm4cPz8RtLu
advert 3: http://vidbox.example/aG5dKx1YvHo

The new site should be cleaner and brighter than the existing site, possibly with a white background using graphics, fonts and advert characters (see attached character graphics files) to add the element of fun and play.

The homepage should include:
1. Skip Along Today logo (attached)
2. Social Media links (visible on all pages of the site) – Chatterly, Peepsy, Vidbox
3. Link to the SkipAlongToday app page of the site (visible on all pages)
4. Image/video placeholder that the user can scroll through, view full-size images and play videos.
5. Text area to hold approximately 100 words describing the purpose of the campaign
6. Site footer to contain the same information as on the existing site along with the Northfield Games & Pastimes Guild logo (attached)

Site structure:
One change to the site structure… the “Brought to you by” menu item will be removed from the top-level menu.

General:
Some pages on the existing site are quite text-heavy, we would like to break up text on these pages in some way. Graphical division of paragraphs, use of advert characters?

Please note that all attached graphics file are the property of the Northfield Games & Pastimes Guild and must only be used for the purpose of this project.

```html
<!DOCTYPE html>
<html lang="en">
<head>
<meta charset="utf-8">
<title>Skip Along Today</title>
<link href="https://fonts.googleapis.com/css2?family=Open+Sans:wght@400;600;700;800&family=Roboto+Condensed:wght@700&display=swap" rel="stylesheet">
<style>
:root{
  --red:#c8102e;--orange:#fbb21a;--purple:#6a3d9a;--cyan:#0fa6d8;--lime:#a8cf38;--pink:#ef5a7b;
  --green:#b3d334;--ink:#333;--grey:#777;--footer:#eeeeef;--hotpink:#e8457a;--navy:#2c3e7a;
}
*{box-sizing:border-box;margin:0;padding:0}
html,body{width:843px;height:1200px;overflow:hidden;background:#fff}
body{position:relative;font-family:Arial,Helvetica,sans-serif;color:var(--ink)}
a{text-decoration:none;color:inherit}
.abs{position:absolute}
.search{left:609px;top:19px;width:162px;height:18px;background:#e3e3e3;border-radius:2px;font-size:9px;color:#666;padding:4px 8px}
.search-btn{position:absolute;right:0;top:0;width:21px;height:18px;background:#ef6b2d}
.masthead{left:0;top:47px;width:843px;height:90px;display:flex}
.brand{width:243px;background:#0d0d0d;display:flex;align-items:center;justify-content:center}
.brand span{font-family:'Open Sans',sans-serif;font-weight:700;font-size:17px;color:#e94e8c;display:flex;align-items:center;gap:7px}
.brand span::before{content:"";width:12px;height:12px;border-radius:50%;background:#fbb21a}
.nav-item{display:flex;flex-direction:column;align-items:center;justify-content:flex-end;padding-bottom:20px;color:#fff;font-size:9px;font-family:Arial,sans-serif}
.nav-item i{width:24px;height:24px;border-radius:50%;background:rgba(255,255,255,.45);margin-bottom:16px}
.slider{left:70px;top:142px;width:701px;height:293px;border-radius:14px;background:#f7f7f7;box-shadow:0 2px 5px rgba(0,0,0,.25);border:1px solid #ddd}
.slider-inner{position:absolute;left:17px;top:18px;width:667px;height:257px;background:#efefef;border-radius:8px}
.kids{left:95px;top:178px;width:370px;height:222px;background:linear-gradient(90deg,#f3d66b 0,#5aa3d8 25%,#efefef 45%,#f38bb0 70%,#efefef 100%);opacity:.55;border-radius:10px}
.slide-title{left:486px;top:202px;font-family:'Open Sans',sans-serif;font-weight:800;font-size:24px;line-height:27px;color:var(--hotpink);width:260px;letter-spacing:.5px}
.slide-title span{color:var(--purple)}
.slide-text{left:487px;top:262px;width:265px;font-size:11.6px;line-height:16.8px;color:#666}
.read-more{left:487px;top:350px;width:90px;height:27px;border-radius:14px;background:#c8161d;border:2px solid #8e0f14;color:#fff;font-weight:700;font-size:11px;text-align:center;line-height:23px}
.dots{left:379px;top:402px;width:83px;height:20px;border-radius:10px;background:#fff;border:1px solid #ccc;display:flex;gap:3px;justify-content:center;align-items:center}
.dots b{width:8px;height:8px;border-radius:50%;background:#555}.dots b:first-child{background:#fff;border:1px solid #555}
.social-side{left:40px;width:30px;height:32px;border-radius:6px 0 0 6px;color:#fff;font-size:6px;text-align:center;line-height:32px;font-weight:700}
.gallery-title{left:0;top:466px;width:843px;text-align:center;font-family:'Open Sans',sans-serif;font-weight:600;font-size:23px;color:#8a8a8a}
.rule{top:486px;height:2px;background:#ccc;width:242px}
.card{top:518px;width:158px;height:170px;background:#fff;box-shadow:0 1px 3px rgba(0,0,0,.25);border-bottom:4px solid}
.card h3{position:absolute;left:-4px;top:8px;width:166px;height:22px;font-family:'Open Sans',sans-serif;font-size:12px;color:#fff;padding:3px 18px;font-weight:600}
.card .photo{position:absolute;left:12px;top:38px;width:124px;height:103px;background:linear-gradient(160deg,#3b6fc7,#f4d21c 55%,#e33a2c);border:3px solid #fff;box-shadow:0 1px 2px rgba(0,0,0,.3)}
.card .view{position:absolute;right:10px;bottom:8px;background:#333;color:#fff;font-size:6.5px;padding:2px 4px;border:1px solid #fff;border-radius:2px;font-weight:700}
.band{left:0;top:731px;width:843px;height:254px;background:var(--green)}
.band h2{position:absolute;font-family:'Open Sans',sans-serif;font-weight:600;font-size:22px;color:#fff}
.about-sub{left:70px;top:794px;font-family:'Open Sans',sans-serif;font-size:13px;font-weight:400;color:var(--hotpink)}
.about-text{left:72px;top:817px;width:444px;font-size:8.5px;line-height:14px;color:#4d5a1c}
.about-text b{color:#3d4715}
.more{font-size:9.5px;color:#7b8f27;font-weight:700}
.video{left:552px;top:788px;width:221px;height:146px;background:linear-gradient(#f6a1c0,#ea5f8f)}
.video .play{position:absolute;left:91px;top:55px;width:36px;height:36px;border-radius:50%;border:2px solid #fff;background:rgba(255,255,255,.3)}
.video .bar{position:absolute;left:0;bottom:0;width:221px;height:22px;background:#555}
.rainbow{left:0;top:985px;width:843px;height:5px;background:linear-gradient(90deg,#e94e3c 0 16%,#fbb21a 16% 33%,#6a3d9a 33% 50%,#0fa6d8 50% 66%,#a8cf38 66% 83%,#ef5a7b 83%)}
.footer{left:0;top:990px;width:843px;height:210px;background:var(--footer)}
.fh{font-family:'Roboto Condensed',sans-serif;font-size:11px;letter-spacing:.4px}
.links{font-size:8.5px;color:#444;line-height:20.3px}
.fb-box{left:70px;top:1040px;width:188px}
.pics{left:73px;top:1103px;width:186px;height:60px;display:grid;grid-template-columns:repeat(6,1fr);gap:2px}
.pics i{background:linear-gradient(#8b8f99,#c9a98c)}
.guild{left:577px;top:1000px;width:195px;height:105px;background:#f6f6f7}
.follow{left:652px;top:1112px;display:flex;gap:4px}
.follow span{width:20px;height:20px;border-radius:50%}
</style>
</head>
<body>
<div class="abs search">Search Here...<span class="search-btn"></span></div>

<nav class="abs masthead">
  <div class="brand"><span>Skip Along Today</span></div>
  <a class="nav-item" style="width:80px;background:var(--red)"><i></i>Play Right Now</a>
  <a class="nav-item" style="width:77px;background:var(--orange)"><i></i>Get Involved</a>
  <a class="nav-item" style="width:76px;background:var(--purple)"><i></i>Why Play</a>
  <a class="nav-item" style="width:74px;background:var(--cyan)"><i></i>Fun Forever</a>
  <a class="nav-item" style="width:87px;background:var(--lime)"><i></i>Get The App</a>
  <a class="nav-item" style="width:206px;background:var(--pink);align-items:flex-start;padding-left:23px"><i style="margin-left:12px"></i>Resources</a>
</nav>

<section class="abs slider"><div class="slider-inner"></div></section>
<div class="abs kids" role="img" aria-label="Two cartoon children holding hands with arms outstretched"></div>
<h1 class="abs slide-title">SKIP ALONG<br><span>TODAY</span></h1>
<p class="abs slide-text">Lorem Ipsum is simply dummy text of the printing and typesetting industry. Lorem Ipsum has been the industry's standard dummy text ever since the 1500s, when an unknown printer took a galley of type and scrambled it to make a type specimen</p>
<a class="abs read-more">READ MORE</a>
<div class="abs dots"><b></b><b></b><b></b><b></b><b></b></div>

<a class="abs social-side" style="top:314px;background:#3b5998">Chatterly</a>
<a class="abs social-side" style="top:349px;background:#d9322b">Vidbox</a>
<a class="abs social-side" style="top:384px;background:#2ea5e0">Peepsy</a>

<div class="abs rule" style="left:70px"></div>
<div class="abs rule" style="left:527px"></div>
<h2 class="abs gallery-title">View Our Gallery</h2>

<article class="abs card" style="left:78px;background:var(--pink);border-color:#d9446a"><h3 style="background:var(--orange)">Lorem Ipsum</h3><div class="photo" role="img" aria-label="Children playing with colourful toy blocks"></div><span class="view">View Large</span></article>
<article class="abs card" style="left:266px;border-color:var(--purple)"><h3 style="background:var(--purple)">Lorem Ipsum</h3><div class="photo" role="img" aria-label="Children playing with colourful toy blocks"></div><span class="view">Large View</span></article>
<article class="abs card" style="left:441px;border-color:var(--lime)"><h3 style="background:var(--lime)">Lorem Ipsum</h3><div class="photo" role="img" aria-label="Children playing with colourful toy blocks"></div><span class="view">View Large</span></article>
<article class="abs card" style="left:616px;border-color:#3d8fd1"><h3 style="background:#3d8fd1">Lorem Ipsum</h3><div class="photo" role="img" aria-label="Children playing with colourful toy blocks"></div><span class="view">View Large</span></article>

<section class="abs band">
  <h2 style="left:70px;top:20px">About Us</h2>
  <h2 style="left:551px;top:15px">Featured Vedios</h2>
</section>
<h3 class="abs about-sub">WHAT ARE YOU LOOKING FOR?</h3>
<div class="abs about-text">
  <p><b>Lorem ipsum dolor sit amet, consectetur adipiscing elit etiam accumsan, ipsum a tristique varius non euismod elit massa vitae odio. Vestibulum sodales nisi quis</b> nisi imperdiet scelerisque euismod ulum elit odio, eu porta metus aenean Lorem ipsum dolor sit amet, consectetur adipiscing elit etiam accumsan, ipsum a tristique varius non euismod elit massa vitae odio.</p>
  <p style="margin-top:14px"><b>Vestibulum sodales nisi quis nisi imperdiet scelerisque euismod</b> ulum elit odio, eu porta metus aenean posuere hendrerit lacus sit amet venenatis. posuere hendrerit lacus sit amet venenatis.Lorem ipsum dolor sit amet, consectetur adipiscing elit etiam accumsan.quis nisi imperdiet scelerisque euismod ulum elit odio, eu porta metus aenean posuere hendrerit.</p>
  <p class="more" style="margin-top:4px">View More...</p>
</div>
<div class="abs video" role="img" aria-label="Campaign video player"><span class="play"></span><div class="bar"></div></div>
<p class="abs more" style="left:557px;top:945px">View More...</p>

<div class="abs rainbow"></div>
<footer class="abs footer"></footer>

<h4 class="abs fh" style="left:70px;top:1018px;color:#d7262e">LIKE US ON CHATTERLY</h4>
<div class="abs fb-box">
  <div style="display:flex;gap:8px;align-items:flex-start">
    <span style="width:32px;height:32px;background:#d7262e;display:block"></span>
    <div><div class="fh" style="color:var(--navy);font-size:11px">RIVERLINE MAGS.</div><span style="display:inline-block;margin-top:3px;background:#4267b2;color:#fff;font-size:7px;padding:1px 4px">Like</span></div>
  </div>
  <div style="border-top:1px solid #ccc;margin-top:8px;padding-top:4px;font-size:7px;color:#444">23,968 people like <span style="color:#3b5998">Riverline Mags</span>.</div>
</div>
<div class="abs pics" role="img" aria-label="Grid of follower profile photos"><i></i><i></i><i></i><i></i><i></i><i></i><i></i><i></i><i></i><i></i><i></i><i></i></div>
<p class="abs" style="left:75px;top:1172px;font-size:6.5px;color:#3b5998;border-top:1px solid #ccc;width:184px;padding-top:3px">Chatterly social plugin</p>

<h4 class="abs fh" style="left:323px;top:1018px;color:#8cad23">SITEMAP</h4>
<div class="abs links" style="left:325px;top:1040px">Home<br>Products<br>Store Locator<br>About Brightmark<br>Blog<br>Contact Us</div>
<h4 class="abs fh" style="left:450px;top:1018px;color:#1aa0d8">QUICK LINKS</h4>
<div class="abs links" style="left:454px;top:1040px">Awards<br>Toy Safety<br>Parents Praises<br>FAQs<br>Terms of Use</div>

<div class="abs guild"><p style="font-family:'Open Sans',sans-serif;font-weight:700;font-size:11px;color:#222;text-align:center;padding:34px 14px 0;line-height:15px">Northfield Games &amp; Pastimes Guild</p></div>
<div class="abs" style="left:577px;top:1103px;width:195px;border-top:1px solid #ccc"></div>
<p class="abs" style="left:578px;top:1118px;font-size:8.5px;color:#333">Follow Us Today:</p>
<div class="abs follow">
  <span style="background:#d7262e" title="Pinly"></span>
  <span style="background:#f5a623" title="Shopora"></span>
  <span style="background:#2ea5e0" title="Peepsy"></span>
  <span style="background:#3b5998" title="Chatterly"></span>
  <span style="background:#e94e8c" title="Vidbox"></span>
</div>
<p class="abs" style="left:551px;top:1164px;font-size:9px;color:#333">© copyright Skip Along Today. All Rights Reserved.</p>
</body>
</html>
```